Derek Mavlow Business card

Hey there, I’m hoping to have a business card designed. I’m in Real estate and just switched to a new Brokerage called: The Property Quarter

The back could just be the company name maybe or whatever looks good!

I’ve attached some logos of our company and some cards my buddy had done up.

On the card:
Derek Mavlow
derekmavlow@postnest.example
587-204-6618
derekmavlow-homes.example

Target Market(s)

Home buyers and sellers

Industry/Entity Type

Real Estate

Contact Information for Business Card

just looking for a cool and modern design with my picture on it. I like the idea of Black and red being used.

Requirements
Must have
• all the details provided. I'm open to anything. Just want a professional looking card.

```html
<!DOCTYPE html>
<html lang="en">
<head>
<meta charset="utf-8">
<title>Derek Mavlow – Business Card</title>
<link rel="stylesheet" href="https://fonts.googleapis.com/css2?family=Montserrat:wght@700;800&family=Lato:wght@400&display=swap">
<style>
  :root {
    --red: #c8203a;
    --black: #060606;
    --white: #ffffff;
    --ink: #1a1a1a;
    --stage: #3a3a3a;
    --suit: #2b3140;
  }
  * { box-sizing: border-box; margin: 0; padding: 0; }
  html, body { width: 1200px; height: 694px; overflow: hidden; }
  body {
    background: var(--stage);
    font-family: "Lato", sans-serif;
    position: relative;
  }
  .card {
    position: absolute;
    top: 193px;
    width: 540px;
    height: 308px;
    overflow: hidden;
    box-shadow: 0 12px 30px rgba(0,0,0,.45);
  }
  /* back side */
  .card-back { left: 40px; background: var(--black); }
  .card-back .brand {
    position: absolute;
    left: 0; right: 0; top: 50%;
    transform: translateY(-50%);
    display: flex; align-items: center; justify-content: center; gap: 16px;
  }
  .brand-mark { width: 22px; height: 22px; background: var(--red); flex: none; }
  .brand-name {
    font-family: "Montserrat", sans-serif;
    font-weight: 800;
    font-size: 52px;
    line-height: 1;
    text-transform: uppercase;
    letter-spacing: -1px;
  }
  .card-back .brand-name { color: var(--white); }

  /* front side */
  .card-front { left: 620px; background: var(--white); }
  .card-front .brand {
    position: absolute; left: 40px; top: 42px;
    display: flex; align-items: center; gap: 12px;
  }
  .card-front .brand-name { color: var(--black); font-size: 38px; }
  .card-front .brand-mark { width: 16px; height: 16px; }
  .portrait {
    position: absolute; right: 0; top: 0;
    width: 190px; height: 300px;
    background: linear-gradient(180deg, #f2f2f2 0%, #c9ccd3 35%, var(--suit) 100%);
  }
  .name-band {
    position: absolute; left: 0; top: 160px;
    width: 390px; height: 44px;
    background: var(--red);
    display: flex; align-items: center;
    padding-left: 40px;
  }
  .agent-name {
    font-family: "Montserrat", sans-serif;
    font-weight: 700;
    font-size: 22px;
    color: var(--white);
  }
  .contacts {
    position: absolute; left: 40px; top: 218px;
    list-style: none;
  }
  .contacts li {
    display: flex; align-items: center; gap: 10px;
    font-size: 14px; color: var(--ink);
    height: 22px;
  }
  .contacts svg { width: 14px; height: 14px; fill: var(--red); flex: none; }
  .edge-stripe {
    position: absolute; left: 0; bottom: 0;
    width: 100%; height: 8px; background: var(--red);
  }
</style>
</head>
<body>
  <section class="card card-back" aria-label="Card back">
    <div class="brand">
      <span class="brand-mark"></span>
      <span class="brand-name">The Property<br>Quarter</span>
    </div>
  </section>

  <section class="card card-front" aria-label="Card front">
    <div class="brand">
      <span class="brand-name">The Property<br>Quarter</span>
      <span class="brand-mark"></span>
    </div>
    <div class="portrait" role="img" aria-label="Portrait photo of Derek Mavlow in a dark blazer and white shirt"></div>
    <div class="name-band"><span class="agent-name">Derek Mavlow</span></div>
    <ul class="contacts">
      <li>
        <svg viewBox="0 0 24 24" aria-hidden="true"><path d="M6.6 10.8a15.1 15.1 0 0 0 6.6 6.6l2.2-2.2a1 1 0 0 1 1-.25 11.4 11.4 0 0 0 3.6.57 1 1 0 0 1 1 1V20a1 1 0 0 1-1 1A17 17 0 0 1 3 4a1 1 0 0 1 1-1h3.5a1 1 0 0 1 1 1c0 1.25.2 2.45.57 3.57a1 1 0 0 1-.25 1z"/></svg>
        587-204-6618
      </li>
      <li>
        <svg viewBox="0 0 24 24" aria-hidden="true"><path d="M2 5h20v14H2z M2 5l10 8 10-8" /></svg>
        derekmavlow@postnest.example
      </li>
      <li>
        <svg viewBox="0 0 24 24" aria-hidden="true"><circle cx="12" cy="12" r="10"/><path d="M2 12h20M12 2c3 3 3 17 0 20M12 2c-3 3-3 17 0 20" stroke="#fff" stroke-width="1.6" fill="none"/></svg>
        derekmavlow-homes.example
      </li>
    </ul>
    <div class="edge-stripe"></div>
  </section>
</body>
</html>
```